Brennick Holdings Business Cards

These are professional business cards that are for my family office.
Put fake emails and phone numbers as of now until I finalize those components. This family office controls my families investments, assets, and future. The cards should be professional.
..
.
.
.
I just uploaded another variation of a logo I would like to see as a business card to I am inbeteen which logo to use

Target Market(s)

business

Industry/Entity Type

business

Contact Information for Business Card

Professional, wealth related, finance related.

Requirements
Must have
• Logo

```html
<!DOCTYPE html>
<html lang="en">
<head>
<meta charset="utf-8">
<title>Brennick Holdings – Business Cards</title>
<link rel="stylesheet" href="https://fonts.googleapis.com/css2?family=Cinzel:wght@500;600&family=Tinos:wght@400;700&display=swap">
<style>
  :root {
    --backdrop: #929192;
    --card: #ffffff;
    --navy: #1a1d2e;
    --accent-light: #f1f1f1;
    --accent-mid: #d4d4d4;
    --text-grey: #9d9d9d;
  }
  * { margin: 0; padding: 0; box-sizing: border-box; }
  html, body {
    width: 1200px; height: 1200px; overflow: hidden;
    background: var(--backdrop);
  }
  .sheet { position: relative; width: 1200px; height: 1200px; }
  .card {
    position: absolute; left: 166px; width: 868px; height: 508px;
    background: var(--card); overflow: hidden;
  }
  .card--front { top: 71px; }
  .card--back { top: 615px; }
  .accent-band { position: absolute; inset: 0; width: 100%; height: 100%; }
  .brand-name {
    position: absolute; font-family: "Cinzel", serif; font-weight: 600;
    color: var(--navy); white-space: nowrap; line-height: 1;
  }
  .card--front .brand-name { left: 90px; top: 92px; font-size: 36px; }
  .card--back .brand-name {
    left: 638px; top: 333px; font-size: 30px; transform: translateX(-50%);
  }
  .brand-circle {
    position: absolute; left: 560px; top: 152px; width: 156px; height: 156px;
    border: 3px solid var(--navy); border-radius: 50%;
  }
  .person {
    position: absolute; left: 90px; top: 256px;
    font-family: "Tinos", serif; color: var(--text-grey);
  }
  .person__name { font-size: 31px; font-weight: 700; letter-spacing: 0.5px; line-height: 1.1; }
  .person__role { font-size: 21px; margin-top: 2px; }
  .contact {
    position: absolute; left: 90px; top: 384px; list-style: none;
    font-family: "Tinos", serif; font-size: 21px; color: var(--text-grey);
  }
  .contact__item { display: flex; align-items: center; height: 33px; }
  .contact__icon { width: 16px; height: 16px; margin-right: 14px; fill: var(--text-grey); }
</style>
</head>
<body>
<main class="sheet">

  <section class="card card--front">
    <svg class="accent-band" viewBox="0 0 868 508" preserveAspectRatio="none" role="img" aria-label="Decorative diagonal bar pattern in black and grey">
      <defs>
        <linearGradient id="bandFront" x1="0" y1="0" x2="1" y2="0">
          <stop offset="0" stop-color="var(--accent-light)"/>
          <stop offset="1" stop-color="var(--accent-mid)"/>
        </linearGradient>
      </defs>
      <polygon points="550,0 868,0 868,508 505,508" fill="url(#bandFront)"/>
    </svg>
    <h1 class="brand-name">Brennick Holdings</h1>
    <div class="person">
      <p class="person__name">ADRIAN KELLER</p>
      <p class="person__role">Director/electrician</p>
    </div>
    <ul class="contact">
      <li class="contact__item">
        <svg class="contact__icon" viewBox="0 0 16 16" aria-hidden="true"><path d="M4 0h8a1.5 1.5 0 0 1 1.5 1.5v13A1.5 1.5 0 0 1 12 16H4a1.5 1.5 0 0 1-1.5-1.5v-13A1.5 1.5 0 0 1 4 0zm0.5 2v10h7V2zM8 13a1 1 0 1 0 0 2 1 1 0 0 0 0-2z"/></svg>
        1234 567 890
      </li>
      <li class="contact__item">
        <svg class="contact__icon" viewBox="0 0 16 16" aria-hidden="true"><path d="M1 3h14v10H1zM1.8 4l6.2 4.6L14.2 4z"/></svg>
        info@brennickholdings.com
      </li>
    </ul>
  </section>

  <section class="card card--back">
    <svg class="accent-band" viewBox="0 0 868 508" preserveAspectRatio="none" role="img" aria-label="Decorative diagonal bar pattern in black and grey">
      <defs>
        <linearGradient id="bandBack" x1="0" y1="0" x2="1" y2="0">
          <stop offset="0" stop-color="var(--accent-mid)"/>
          <stop offset="1" stop-color="var(--accent-light)"/>
        </linearGradient>
      </defs>
      <polygon points="0,0 330,0 310,508 0,508" fill="url(#bandBack)"/>
    </svg>
    <div class="brand-circle" aria-hidden="true"></div>
    <p class="brand-name">Brennick Holdings</p>
  </section>

</main>
</body>
</html>
```